New Fun, Positive, energised looking Business Card Needed for High Achiever Coach

I am looking for a two sided full colour business card. I am self employed and have recently re branded my 1-2-1 work re-vitalising high achievers. My target client base for these cards is therefore high achievers - usually aged 40 -55, they are often entrepreneurs, CEO or work in banking and finance and 2/3 are male. I work with them on 90 day or 6 month coaching programs to help them live their success in a healthier, more sustainable and fulfiiled way. They pay for this privately so though they are corporate types the cards need not look 'corporate'. I want to portray the idea of transformation, vitality and re-connecting.
You can get a feel for the look I like on my new website: norvemitch.co.uk
I want to use this logo with strapline (Re-Vitalising High Achievers) (I purchased off Glyphmart) and font/ colours (the turquoise and green).
Details to include on the card:
www.norvemitch.co.uk
+44 7915 302684
petra@norvemitch.co.uk
skype: norvemitch
I'd also like to include:
Do you struggle to switch off? Want to be healthier and feel fitter? Want closer relationships? More clarity over the direction you are headed? I can help you do these things using integrated mind-body techniques. Visit norvemitch.co.uk TODAY to apply for a FREE Breakthrough session.
BUT if that is too much text for a card I am open to advice/ammendments.
Updates
Thanks for your design - I am considering them. PLease change the wording to :

```html
<!DOCTYPE html>
<html lang="en">
<head>
<meta charset="utf-8">
<title>Petra Norvemitch – Business Card</title>
<link rel="stylesheet" href="https://fonts.googleapis.com/css2?family=Nunito:wght@800&family=Open+Sans:wght@400;700&display=swap">
<style>
  :root {
    --board: #6d6e71;
    --paper: #f4f4f5;
    --turquoise: #05a3cc;
    --green: #5cb85f;
    --white: #ffffff;
  }
  * { margin: 0; padding: 0; box-sizing: border-box; }
  html, body { width: 1025px; height: 1200px; overflow: hidden; }
  body { background: var(--board); position: relative; font-family: "Open Sans", sans-serif; }

  .card { position: absolute; width: 957px; overflow: hidden; background: var(--paper); }
  .card-front { left: 33px; top: 33px; height: 541px; }
  .card-back { left: 25px; top: 618px; height: 545px; }
  .card-shapes { position: absolute; inset: 0; width: 100%; height: 100%; }

  .brand-mark { position: absolute; left: 50%; top: 50px; width: 130px; height: 130px; margin-left: -65px; border-radius: 50%; background: var(--green); }
  .brand { position: absolute; left: 0; right: 0; top: 232px; text-align: center; font-family: "Nunito", sans-serif; font-weight: 800; color: var(--turquoise); }
  .brand-name { display: inline-block; padding: 0 16px; background: var(--paper); border-radius: 10px; font-size: 46px; line-height: 60px; }
  .brand-strapline { display: block; font-size: 24px; line-height: 32px; margin-top: 2px; }

  .contact-list { position: absolute; left: 322px; top: 386px; list-style: none; color: var(--white); font-size: 26px; line-height: 34px; }
  .contact-list li { display: flex; align-items: center; gap: 12px; height: 34px; }
  .contact-list li + li { margin-top: -1px; }
  .contact-icon { width: 22px; height: 22px; flex: none; }
  .contact-list li:nth-child(1) .contact-icon { margin-right: -10px; }

  .pitch { position: absolute; left: 40px; right: 40px; top: 362px; text-align: center; color: var(--green); font-size: 22px; line-height: 31px; }
  .pitch-link { color: var(--turquoise); font-weight: 700; font-size: 25px; }
</style>
</head>
<body>

<section class="card card-front" aria-label="Front of card">
  <svg class="card-shapes" viewBox="0 0 957 541" preserveAspectRatio="none" aria-hidden="true">
    <path d="M0 40 C 140 330 330 368 478 368 C 626 368 816 330 957 40 L957 541 L0 541 Z" fill="var(--turquoise)"/>
    <path d="M0 70 C 130 300 320 338 478 338 C 636 338 827 300 957 70 C 830 312 640 352 478 352 C 316 352 126 312 0 70 Z" fill="var(--green)"/>
  </svg>
  <div class="brand-mark" aria-hidden="true"></div>
  <div class="brand">
    <span class="brand-name">Petra Norvemitch</span>
    <span class="brand-strapline">Re-Vitalising High Achievers</span>
  </div>
  <ul class="contact-list">
    <li>
      <svg class="contact-icon" viewBox="0 0 24 24" aria-hidden="true"><path fill="var(--white)" d="M3 9c0-3 4-5 9-5s9 2 9 5l-4 1-1-2c-2-1-6-1-8 0L7 10zM6 12h12l2 8H4z"/><circle cx="12" cy="16" r="2.4" fill="var(--turquoise)"/></svg>
      <span>+44 7915 302684</span>
    </li>
    <li>
      <svg class="contact-icon" viewBox="0 0 24 24" aria-hidden="true"><circle cx="12" cy="12" r="10" fill="var(--white)"/></svg>
      <span>norvemitch</span>
    </li>
    <li>
      <svg class="contact-icon" viewBox="0 0 24 24" aria-hidden="true"><circle cx="12" cy="12" r="10" fill="none" stroke="var(--white)" stroke-width="2"/><ellipse cx="12" cy="12" rx="4.5" ry="10" fill="none" stroke="var(--white)" stroke-width="2"/><path d="M2 12h20M4 7h16M4 17h16" stroke="var(--white)" stroke-width="1.6"/></svg>
      <span>www.norvemitch.co.uk</span>
    </li>
    <li>
      <svg class="contact-icon" viewBox="0 0 24 24" aria-hidden="true"><rect x="2" y="5" width="20" height="14" fill="var(--white)"/><path d="M2 5l10 8 10-8" fill="none" stroke="var(--turquoise)" stroke-width="1.8"/></svg>
      <span>petra@norvemitch.co.uk</span>
    </li>
  </ul>
</section>

<section class="card card-back" aria-label="Back of card">
  <svg class="card-shapes" viewBox="0 0 957 545" preserveAspectRatio="none" aria-hidden="true">
    <path d="M0 0 L957 0 L957 40 C 820 150 640 192 478 192 C 316 192 136 150 0 40 Z" fill="var(--turquoise)"/>
    <path d="M0 60 C 130 190 320 212 478 212 C 636 212 827 190 957 60 C 840 208 640 230 478 230 C 316 230 116 208 0 60 Z" fill="var(--turquoise)"/>
  </svg>
  <p class="pitch">
    Do you struggle to switch off? Want to be healthier and feel fitter? Want closer relationships? More clarity over the direction you are headed? I can help you do these things using integrated mind-body techniques.<br>
    Visit <span class="pitch-link">norvemitch.co.uk</span><br>
    TODAY to apply for a FREE Breakthrough session.
  </p>
</section>

</body>
</html>
```